Math Help Website Needs New Design

Looking to refresh the design of my existing site (quillnumberdesk.com) to be easier on the eyes. I am fully capable of doing the HTML coding and have for years, but I don't have the eye for good design, colors, layout, and fonts. This is where I need help!

I need both a new design scheme and a new logo that matches. The overall functionality will be the same as the existing site, and should not be unrecognizable.

Target Market(s)

It should appeal to students (age 13-22) and their parents, so it should NOT be childish in appearance, nor should it be corporate.

Requirements
Must have
• Should be simple, easy-to-navigate, and neither childish nor corporate. I am looking for a design for both the homepage and a similar "content" page. Simple, bold colors are preferred. A logo should be prominent at the top, with a search bar nearby. Below that I need a similar navigational area like I already have. Then, I need about 200px wide ad space on the left of the main body area.

```html
<!DOCTYPE html>
<html lang="en">
<head>
<meta charset="utf-8">
<title>Quill Number Desk – Geometry Lessons</title>
<link href="https://fonts.googleapis.com/css2?family=Arimo:wght@400;700&family=Bree+Serif&display=swap" rel="stylesheet">
<style>
:root{
  --navy:#1f2a5f;
  --steel:#6e90b9;
  --deep:#2c4486;
  --deep2:#223773;
  --lime:#a6d51d;
  --sun:#f7d600;
  --sky:#2ea2d8;
  --orange:#f7931e;
  --red:#e7251f;
  --grey-ad:#c9c9c9;
  --ink:#555a63;
  --title:#1f2a5f;
  --btn:#3e5592;
  --field:#e9eef6;
}
*{box-sizing:border-box;margin:0;padding:0}
html,body{width:997px;height:1200px;overflow:hidden;background:var(--navy)}
body{font-family:Arimo,Arial,sans-serif}
.page{position:absolute;left:0;top:0;width:1230px;height:1480px;transform:scale(.8106);transform-origin:0 0;background:var(--deep)}
.abs{position:absolute}
.topbar{left:0;top:0;width:1230px;height:28px;background:var(--navy)}
.topbar a{position:absolute;right:122px;top:6px;color:#fff;font-weight:700;font-size:14px;text-decoration:none}
.header{left:0;top:28px;width:1230px;height:188px;background:var(--steel)}
.brand{left:118px;top:98px;display:flex;align-items:center;gap:12px;color:#fff;font-weight:700;font-size:38px;letter-spacing:.5px}
.brand .dot{width:30px;height:30px;border-radius:50%;background:#fff}
.search{left:897px;top:78px;width:214px;height:30px;background:#b9cade;border:1px solid #d9e3ef;border-radius:3px;color:#fff;font-size:12px;padding:8px 0 0 18px}
.search svg{position:absolute;right:6px;top:4px}
.tabs{left:472px;top:138px;height:40px;display:flex}
.tab{height:40px;color:#fff;font-weight:700;font-size:15px;display:flex;align-items:center;justify-content:center;border-radius:8px 8px 0 0;margin-right:-2px}
.tab.home{width:70px;background:var(--sun)}
.tab.text{width:155px;background:var(--lime)}
.tab.video{width:150px;background:var(--sky)}
.tab.more{width:147px;background:var(--orange)}
.tab.forum{width:110px;background:var(--red)}
.subnav{left:302px;top:178px;width:812px;height:38px;background:var(--lime)}
.subnav span{position:absolute;top:12px;color:#fff;font-weight:700;font-size:14px}
.subnav .on{border-bottom:2px solid #fff;padding-bottom:1px}
.body-bg{left:0;top:216px;width:1230px;height:909px;background:linear-gradient(180deg,var(--deep2),var(--deep) 60%,#34508f)}
.adbox{background:var(--grey-ad);border:5px solid #fff}
.adbox span{position:absolute;left:50%;top:50%;transform:translate(-50%,-50%) rotate(-90deg);color:#fff;font-size:44px;white-space:nowrap}
.main{left:303px;top:216px;width:811px;height:636px;background:#fff}
.title{left:724px;top:230px;font-family:"Bree Serif",Georgia,serif;font-size:21px;color:var(--title)}
.list{width:292px;list-style:none}
.list li{height:28.6px;border-bottom:1px solid #4a4a4a;color:var(--ink);font-size:14px;padding:6px 0 0 12px}
.list li:last-child{border-bottom:none}
.mascot{left:1095px;top:245px;width:135px;height:235px;border-radius:40px 0 0 20px;background:linear-gradient(180deg,#e9b98c,#6a8fb4)}
.ask{left:303px;top:879px;width:808px;height:217px;background:#fff}
.callout{left:324px;top:835px;width:241px;height:62px;background:var(--orange);border:2px solid #fff;color:#fff;font-family:"Bree Serif",Georgia,serif;font-size:19px;line-height:23px;text-align:center;padding-top:6px;letter-spacing:1px}
.reader{left:312px;top:900px;width:300px;height:235px;border-radius:50% 50% 10px 10px;background:linear-gradient(160deg,#f1d7b8,#6d9ccf 60%,#ededed)}
.note{left:591px;top:910px;width:215px;font-size:12.5px;line-height:16px;color:var(--ink)}
.lbl{font-size:12.5px;color:var(--ink)}
.field{background:var(--field);border:1px solid #9fb0c9;border-radius:4px}
.btn{height:18px;background:var(--btn);color:#fff;font-size:12px;padding:2px 0 0 10px;border-radius:2px}
.footer{left:0;top:1125px;width:1230px;height:270px;background:var(--steel)}
.fcol{top:1150px;list-style:none;color:#fff;font-size:16.5px;line-height:26px}
.fcol .h{color:#eef3fa;text-transform:uppercase}
.vline{top:1155px;width:1px;height:225px;background:#fff}
.bottom{left:0;top:1395px;width:1230px;height:85px;background:var(--navy);border-top:1px solid #9fb3cf}
.legal{left:134px;top:1407px;color:#fff;font-size:14px}
.copy{left:809px;top:1408px;color:#fff;font-size:14px}
</style>
</head>
<body>
<div class="page">
  <div class="abs topbar"><a href="#">REGISTER / SIGN IN</a></div>
  <div class="abs header"></div>
  <div class="abs brand"><span class="dot"></span>quillnumberdesk</div>
  <div class="abs search">Search the site...
    <svg width="20" height="20" viewBox="0 0 20 20"><circle cx="11" cy="8" r="6" fill="none" stroke="#fff" stroke-width="2"/><line x1="7" y1="12" x2="2" y2="17" stroke="#fff" stroke-width="2.5"/></svg>
  </div>
  <nav class="abs tabs">
    <div class="tab home"><svg width="26" height="22" viewBox="0 0 26 22"><path d="M13 1 1 11h4v10h6v-6h4v6h6V11h4z" fill="#fff"/></svg></div>
    <div class="tab text">TEXT LESSONS</div>
    <div class="tab video">VIDEO LESSONS</div>
    <div class="tab more">MORE SUBJECTS</div>
    <div class="tab forum">FORUM</div>
  </nav>
  <nav class="abs subnav">
    <span style="left:79px">ALGEBRA</span>
    <span class="on" style="left:195px">GEOMETRY</span>
    <span style="left:335px">TRIGONOMETRY</span>
    <span style="left:511px">CALCULUS</span>
    <span style="left:659px">STATISTICS</span>
  </nav>

  <div class="abs body-bg"></div>
  <div class="abs adbox" style="left:113px;top:237px;width:172px;height:610px"><span>ADVERTISEMENT</span></div>
  <div class="abs adbox" style="left:113px;top:865px;width:172px;height:230px"><span>AD</span></div>

  <main class="abs main"></main>
  <h1 class="abs title">Mr. Alder's Lessons</h1>
  <ul class="abs list" style="left:353px;top:287px">
    <li>30-60-90 Right Triangle</li><li>Asymptotes</li><li>Completing the Square In Circle Equations</li><li>Distance Formula</li><li>Domain and Range</li><li>Finding Asymptotes</li><li>Finding Horizontal Asymptotes</li><li>Geometric Mean</li><li>Length of a Line Segment</li><li>Midpoint Formula</li><li>Point Slope Form</li><li>Slope Intercept Form</li><li>Slope of a Line</li>
  </ul>
  <ul class="abs list" style="left:711px;top:287px">
    <li>1.2 - Geometric Terms</li><li>1.3 - Geometry Vocabulary</li><li>1.4 - World of Angles</li><li>2.1 - Special Angles</li><li>2.2 - Parallel Lines</li><li>2.3 - Polygons</li><li>2.4 - Sum of the Angles of a Triangle</li><li>2.5 - Exterior Angles of a Triangle</li><li>3.1 - Interior Angles of a Polygon</li><li>3.2 - Congruent Triangles</li><li>3.3 - Isosceles Triangles</li><li>3.4 - Triangle Inequalities</li><li>4.1 - Parallelograms</li><li>4.2 - Trapezoids</li><li>4.3 - Special Parallelograms</li>
  </ul>
  <div class="abs mascot" role="img" aria-label="Photo of a boy in glasses peeking around the lesson panel"></div>

  <section class="abs ask"></section>
  <div class="abs reader" role="img" aria-label="Photo of a boy in glasses lying down writing in a notebook"></div>
  <svg class="abs" style="left:360px;top:895px" width="60" height="40"><path d="M2 0h50L40 38z" fill="#f7931e"/></svg>
  <div class="abs callout">ASK YOUR QUESTION<br>MESSAGE BOARD</div>
  <p class="abs note">Register and Sign in to get your questions answered by our friendly Forum volunteers.</p>
  <span class="abs lbl" style="left:592px;top:989px">User Name:</span>
  <span class="abs lbl" style="left:592px;top:1019px">Password:</span>
  <div class="abs field" style="left:670px;top:986px;width:148px;height:24px"></div>
  <div class="abs field" style="left:670px;top:1017px;width:148px;height:24px"></div>
  <div class="abs field" style="left:848px;top:894px;width:237px;height:149px;background:#f4f5f7;border-color:#cfd6e0"></div>
  <div class="abs btn" style="left:594px;top:1055px;width:80px">SIGN IN &#10095;</div>
  <div class="abs btn" style="left:726px;top:1055px;width:90px">REGISTER &#10095;</div>
  <div class="abs btn" style="left:851px;top:1055px;width:169px">SUMBIT YOUR QUESTION &#10095;</div>

  <footer class="abs footer"></footer>
  <ul class="abs fcol" style="left:325px"><li class="h">Free Math Resources</li><li>Mr. Alder's Lessons</li><li>Algebra Lessons</li><li>Geometry Lessons</li><li>Trigonometry Lessons</li><li>Calculus Lessons</li><li>Statistics Lessons</li><li>Sports Math</li></ul>
  <div class="abs vline" style="left:575px"></div>
  <ul class="abs fcol" style="left:606px"><li class="h">Free Calculators Help</li><li>Equation Solver</li><li>Equation Grapher</li><li>Derivative Calculator</li><li>Factoring Calculator</li><li>Integral Calculator</li></ul>
  <div class="abs vline" style="left:855px"></div>
  <ul class="abs fcol" style="left:885px"><li class="h">More Subjects</li><li>Ask an Expert</li><li>Books</li><li>Calculator Buying Guide</li><li>Famous Mathematicialns</li><li>Origins of Math</li><li>Math Games</li><li>Glossary</li><li>Study Tips</li></ul>

  <div class="abs bottom"></div>
  <p class="abs legal">Terms of Use &nbsp;|&nbsp; Privacy Policy &nbsp;|&nbsp; Contact Us &nbsp;|&nbsp; About Us &nbsp;|&nbsp; Download PDF Viewer</p>
  <p class="abs copy">Quill Number Desk © 2013 All Rights Reserved</p>
</div>
</body>
</html>
```